Marketplace App for Gamers needs Brand Identity

You are competing to produce the Brand Identity for Pelvora, a new marketplace app for Kestra OS and Verdant OS. Pelvora is specific to the gaming industry, providing a platform for gaming enthusiasts to buy, sell and trade PC and console games as well as gaming hardware.

This project requires production of a logo, single-page marketing website and user interface design for the mobile application. All outputs should be as PSD files so they can be easily included into the mobile application by our developers.

The successful design will communicate modernity, edginess and and a sense of belonging to the gaming community. Attached is a logo we are fond of (but not attached to). It is a fusion of a hawk and micro chip. The text font is ideal.

Desired colours are shades of greens, blues or purples. Gray may be included with any of these three but we are not keen to mix green with purple.

About Us

Pelvora is being developer by Brantel Holdings. Our focus is on building mobile first e-commerce applications with millennials and other digital natives in mind.

Industry/Entity Type

Industry

Number of Pages Required

1 page

Font styles to use
Sans Serif

Colors
3276b5
33b8a4
886aae

```html
<!DOCTYPE html>
<html lang="en">
<head>
<meta charset="utf-8">
<title>Pelvora – Trading games just became easier</title>
<link rel="stylesheet" href="https://fonts.googleapis.com/css2?family=Michroma&family=Arimo:wght@400;700&family=Playfair+Display:wght@400;700&family=Anton&display=swap">
<style>
:root{
  --bg:#000;
  --page:#121212;
  --panel:#171717;
  --purple:#886aae;
  --purple-deep:#4e3b78;
  --purple-glow:#a48ad6;
  --steel:#3a3a3a;
  --steel-light:#6a6a6a;
  --text:#ffffff;
  --muted:#cfcfcf;
  --line:#8a8a8a;
}
*{margin:0;padding:0;box-sizing:border-box}
html,body{width:1200px;height:1000px;overflow:hidden;background:var(--bg)}
body{position:relative;font-family:"Arimo",Arial,sans-serif;color:var(--text)}
.page{position:absolute;left:326px;top:0;width:547px;height:1000px;background:var(--page);overflow:hidden}
.abs{position:absolute}
.display{font-family:"Michroma",Arial,sans-serif;letter-spacing:.06em}

/* top and bottom bars */
.bar{position:absolute;left:0;width:547px;background:linear-gradient(#1c1c1c,#080808);}
.bar .glow-l,.bar .glow-r{position:absolute;width:120px;height:4px;background:linear-gradient(90deg,transparent,var(--purple-glow),transparent);filter:blur(1px)}
.topbar{top:0;height:38px}
.topbar .glow-l{left:0;top:8px}.topbar .glow-r{right:0;top:8px}
.topbar .edge{position:absolute;left:0;right:0;bottom:0;height:2px;background:#e6e6e6}
.nav{position:absolute;top:15px;left:150px;width:250px;display:flex;justify-content:center;font-size:6px;letter-spacing:.05em;color:var(--muted)}
.nav a{color:inherit;text-decoration:none;padding:3px 10px;border-right:1px solid #777}
.nav a:last-child{border-right:0}
.nav a.is-active{border-bottom:1px solid #ddd}

/* hero */
.hero{position:absolute;top:38px;left:0;width:547px;height:240px;
  background:radial-gradient(ellipse at 45% 40%,#7a62a6 0%,#5b4585 45%,#3e2d5f 100%)}
.hero .edge{position:absolute;left:46px;right:46px;bottom:0;height:2px;background:#e6e6e6}
.brand{font-family:"Michroma",Arial,sans-serif;color:var(--text);font-weight:400}
.hero .brand{left:46px;top:35px;font-size:25px;letter-spacing:.04em}
.tagline{left:46px;top:71px;font-family:"Michroma",Arial,sans-serif;font-size:8.5px;letter-spacing:.06em}
.tagline b{color:#1a1a1a;font-weight:400}
.hero-copy{left:46px;top:88px;width:210px;font-size:6.3px;line-height:9.5px;color:#eee;text-align:justify}
.cta{top:140px;height:25px;display:flex;align-items:center;justify-content:center;font-size:6.5px;font-weight:700;letter-spacing:.05em}
.cta-learn{left:46px;width:68px;background:#fff;color:#111}
.cta-store{left:114px;width:67px;background:#9a9a9a}
.cta-play{left:181px;width:67px;background:#0c0c0c}
.badge-shape{width:42px;height:11px;border-radius:2px;background:rgba(255,255,255,.35)}
.placeholder{left:380px;top:229px;font-size:5px;color:#bbb}

/* section bands */
.band{position:absolute;left:0;width:547px;background:linear-gradient(#2a2a2a,#0d0d0d);border-top:1px solid #444;border-bottom:1px solid #444}
.band-plate{position:absolute;left:95px;width:357px;top:4px;bottom:4px;background:linear-gradient(#777,#3a3a3a);
  clip-path:polygon(4% 0,96% 0,100% 50%,96% 100%,4% 100%,0 50%)}
.band-tab{position:absolute;left:122px;width:302px;top:3px;bottom:3px;background:linear-gradient(#a78bd1,var(--purple) 55%,#6b4f95);
  clip-path:polygon(3% 0,97% 0,100% 50%,97% 100%,3% 100%,0 50%);
  display:flex;align-items:center;justify-content:center;font-family:"Michroma",Arial,sans-serif;font-size:11px;letter-spacing:.07em;color:#fff}

/* content sections */
.section{position:absolute;left:0;width:547px;background:repeating-linear-gradient(45deg,#181818 0 2px,#121212 2px 4px)}
.divider{position:absolute;left:273px;width:2px;background:#9a9a9a}
.feature-image{border:1px solid var(--purple-glow);box-shadow:0 0 10px 2px rgba(164,138,214,.7)}
.feature-heading{font-family:"Michroma",Arial,sans-serif;font-size:8.5px;letter-spacing:.06em}
.feature-copy{width:200px;font-size:6.2px;line-height:10.6px;color:#ddd;text-align:justify}

/* press */
.press-title{left:0;width:547px;text-align:center;font-family:"Michroma",Arial,sans-serif;font-size:8px;letter-spacing:.08em}
.rule{left:46px;width:455px;height:1px;background:#d8d8d8}
.press-row{left:46px;width:455px;top:738px;height:30px;display:flex;justify-content:space-between;align-items:center}
.press-name{font-family:"Michroma",Arial,sans-serif;font-size:9px;letter-spacing:.05em;color:#fff}

/* footer */
.footer{position:absolute;left:0;top:800px;width:547px;height:168px;background:#050505}
.footer .brand{left:46px;top:22px;font-size:22px;letter-spacing:.04em}
.footer-copy{left:46px;top:55px;width:200px;font-size:6.2px;line-height:10.6px;color:#ddd;text-align:justify}
.link-col{top:42px;width:70px}
.link-col h4{font-family:"Michroma",Arial,sans-serif;font-size:8px;font-weight:400;letter-spacing:.05em;margin-bottom:4px}
.link-col li{list-style:none;font-size:6.4px;line-height:10.4px;color:#ddd}
.bottombar{top:968px;height:32px}
.bottombar .glow-l{left:0;top:2px}.bottombar .glow-r{right:0;top:2px}
.copyright{position:absolute;top:20px;width:547px;text-align:center;font-size:5px;color:#aaa;letter-spacing:.05em}
</style>
</head>
<body>
<div class="page">

  <header class="bar topbar">
    <span class="glow-l"></span><span class="glow-r"></span>
    <nav class="nav">
      <a href="#">MEDIA</a><a href="#" class="is-active">MORE INFO</a><a href="#">HOME</a><a href="#">COMMUNITY</a><a href="#">ABOUT US</a>
    </nav>
    <span class="edge"></span>
  </header>

  <section class="hero" role="img" aria-label="Purple-tinted armoured game character artwork as hero backdrop">
    <div class="abs brand">PELVORA</div>
    <div class="abs tagline">TRADING <b>GAMES</b> JUST BECAME <b>EASIER</b></div>
    <p class="abs hero-copy">A new marketplace app for Kestra OS and Verdant OS. Pelvora is specific to the gaming industry, providing a platform for gaming enthusiasts to buy, sell and trade PC and console games as well as gaming hardware.</p>
    <a class="abs cta cta-learn">LEARN MORE</a>
    <span class="abs cta cta-store"><span class="badge-shape"></span></span>
    <span class="abs cta cta-play"><span class="badge-shape"></span></span>
    <svg class="abs" style="left:355px;top:84px" width="145" height="156" viewBox="0 0 145 156" aria-hidden="true">
      <rect x="60" y="1" width="83" height="160" rx="9" fill="#e9e9e9" stroke="#bbb"/>
      <rect x="66" y="18" width="71" height="140" fill="#111"/>
      <rect x="7" y="18" width="78" height="150" rx="9" fill="#f2f2f2" stroke="#bbb"/>
      <rect x="13" y="37" width="66" height="125" fill="#111"/>
      <circle cx="46" cy="27" r="1.5" fill="#999"/>
    </svg>
    <span class="abs placeholder">place holder</span>
    <span class="edge"></span>
  </section>

  <div class="band" style="top:292px;height:46px"><div class="band-plate" style="top:12px;bottom:8px"></div><div class="band-tab" style="top:13px;bottom:10px">TRADE GAMES</div></div>

  <section class="section" style="top:338px;height:147px">
    <div class="abs feature-image" style="left:47px;top:22px;width:200px;height:100px;background:linear-gradient(160deg,#bfc2b8 0%,#6f7468 35%,#3b3f38 70%,#1d1f1c 100%)" role="img" aria-label="Battlefield scene from a first-person shooter game"></div>
    <span class="divider" style="top:0;height:137px"></span>
    <div class="abs feature-heading" style="left:299px;top:20px">HEADING</div>
    <p class="abs feature-copy" style="left:299px;top:37px">"Lorem ipsum dolor sit amet, consectetur adipiscing elit, sed do eiusmod tempor incididunt ut labore et dolore magna aliqua. Ut enim ad minim veniam, quis nostrud exercitation ullamco laboris nisi ut aliquip ex ea commodo consequat. Duis aute irure dolor in reprehenderit in voluptate velit esse cillum dolore eu fugiat nulla pariatur. Excepteur sint occaecat cupidatat non proident, sunt in culpa qui officia deserunt mollit anim id est laborum."</p>
  </section>

  <div class="band" style="top:485px;height:30px"><div class="band-plate"></div><div class="band-tab">TRADE HARDWARE</div></div>

  <section class="section" style="top:515px;height:153px">
    <div class="abs feature-heading" style="left:46px;top:25px">HEADING</div>
    <p class="abs feature-copy" style="left:46px;top:42px">"Lorem ipsum dolor sit amet, consectetur adipiscing elit, sed do eiusmod tempor incididunt ut labore et dolore magna aliqua. Ut enim ad minim veniam, quis nostrud exercitation ullamco laboris nisi ut aliquip ex ea commodo consequat. Duis aute irure dolor in reprehenderit in voluptate velit esse cillum dolore eu fugiat nulla pariatur. Excepteur sint occaecat cupidatat non proident, sunt in culpa qui officia deserunt mollit anim id est laborum."</p>
    <span class="divider" style="top:6px;height:140px"></span>
    <div class="abs feature-image" style="left:300px;top:27px;width:200px;height:98px;background:radial-gradient(circle at 35% 50%,#3a2a2a 0%,#1e1818 40%,#0c0c0c 100%)" role="img" aria-label="Gaming graphics card with twin cooling fans"></div>
  </section>

  <div class="band" style="top:668px;height:27px"><div class="band-plate"></div><div class="band-tab">ABOUT</div></div>

  <section class="section" style="top:695px;height:105px;background:#141414">
    <div class="abs press-title" style="top:13px">FEATURED IN</div>
    <span class="abs rule" style="top:28px"></span>
    <span class="abs rule" style="top:89px"></span>
  </section>
  <div class="abs press-row">
    <span class="press-name">NORTHGATE</span><span class="press-name">BYTEWIRE</span><span class="press-name">TESSEL</span><span class="press-name">LEDGER</span><span class="press-name">NWR</span>
  </div>

  <footer class="footer">
    <div class="abs brand">PELVORA</div>
    <p class="abs footer-copy">"Lorem ipsum dolor sit amet, consectetur adipiscing elit, sed do eiusmod tempor incididunt ut labore et dolore magna aliqua. Ut enim ad minim veniam, quis nostrud exercitation ullamco laboris nisi ut aliquip ex ea commodo consequat. Duis aute irure dolor in reprehenderit in voluptate velit esse cillum dolore eu fugiat nulla pariatur. Excepteur sint occaecat cupidatat non proident, sunt in culpa qui officia deserunt mollit anim id est laborum."</p>
    <div class="abs link-col" style="left:275px"><h4>SITE MAP</h4><ul><li>MEDIA</li><li>MORE INFO</li><li>HOME</li><li>CMMUNITY</li><li>ABOUT US</li></ul></div>
    <div class="abs link-col" style="left:349px"><h4>HEADING</h4><ul><li>MEDIA</li><li>MORE INFO</li><li>HOME</li><li>CMMUNITY</li><li>ABOUT US</li></ul></div>
    <div class="abs link-col" style="left:425px"><h4>HEADING</h4><ul><li>MEDIA</li><li>MORE INFO</li><li>HOME</li><li>CMMUNITY</li><li>ABOUT US</li></ul></div>
  </footer>

  <div class="bar bottombar">
    <span class="glow-l"></span><span class="glow-r"></span>
    <div class="copyright">COPYWRITE INFO</div>
  </div>

</div>
</body>
</html>
```